Redesign business card for Mark Delaney Construction

Basically I want a complete redesign of the business card I have attached with this project. The only stipulations I have are that the colors , crimson and white, stay the same and all of the information on the old card is also on the new design. Also I would like to add that we also specialize in metal building foundations as well. I look forward to seeing what you all come up with.
Industry/Entity Type
Business
Contact Information for Business Card
All of the details are on the attachment I have included with this project

```html
<!DOCTYPE html>
<html lang="en">
<head>
<meta charset="utf-8">
<title>Mark Delaney Construction – Business Card</title>
<link rel="stylesheet" href="https://fonts.googleapis.com/css2?family=Mulish:ital,wght@0,400;0,700;0,800;1,400&family=Tinos&display=swap">
<style>
  :root {
    --crimson: #ec1f27;
    --maroon: #6b0f1a;
    --white: #ffffff;
    --border: #9a9a9a;
    --ink: #222222;
  }
  * { margin: 0; padding: 0; box-sizing: border-box; }
  html, body { width: 849px; height: 1200px; overflow: hidden; background: var(--white); }
  body { position: relative; font-family: "Mulish", Arial, sans-serif; }

  .card {
    position: absolute;
    left: 144px;
    width: 539px;
    height: 315px;
    border: 1px solid var(--border);
    background: var(--white);
    overflow: hidden;
  }
  .card--front { top: 192px; }
  .card--back { top: 621px; }
  .card__shapes { position: absolute; inset: 0; }

  .side-label {
    position: absolute;
    left: 0; width: 849px;
    text-align: center;
    font-family: "Tinos", "Times New Roman", serif;
    font-size: 14px;
    letter-spacing: 0.5px;
    color: var(--ink);
  }
  .side-label--front { top: 527px; }
  .side-label--back { top: 958px; }

  /* front: header */
  .company {
    position: absolute; left: 44px; top: 45px;
    color: var(--white); font-weight: 800; text-transform: uppercase;
    line-height: 1.2;
  }
  .company__name { font-size: 13.5px; }
  .company__trade { font-size: 12.5px; }
  .owner {
    position: absolute; left: 44px; top: 87px;
    color: var(--white); font-size: 16px; font-weight: 800;
  }
  .owner__role { font-weight: 400; font-style: italic; font-size: 14px; margin-left: 6px; }

  /* front: contact rows */
  .contact-row { position: absolute; left: 1px; display: flex; align-items: center; }
  .contact-row__label {
    width: 96px; height: 100%;
    background: var(--maroon); color: var(--white);
    font-size: 11px; font-weight: 700;
    display: flex; align-items: center; justify-content: flex-end;
    padding-right: 8px;
  }
  .contact-row__value {
    padding-left: 9px; color: var(--white);
    font-size: 11px; font-weight: 800; line-height: 1.2;
  }

  /* front: brand block */
  .brand {
    position: absolute; left: 376px; top: 66px; width: 130px;
    text-align: center; color: var(--crimson);
  }
  .brand__mark {
    width: 64px; height: 64px; margin: 0 auto;
    border: 5px solid var(--crimson); border-radius: 50%;
  }
  .brand__name { margin-top: 10px; font-size: 10.5px; font-weight: 700; text-transform: uppercase; line-height: 1.25; }
  .founder {
    position: absolute; left: 356px; top: 190px; width: 170px;
    text-align: center; color: var(--crimson); line-height: 1.25;
  }
  .founder__title { font-size: 13px; font-weight: 400; }
  .founder__name { font-size: 18px; font-weight: 800; }
  .founder__nick { font-size: 13px; font-weight: 400; letter-spacing: 0.5px; }

  /* back */
  .specialty-heading {
    position: absolute; left: 42px; top: 147px;
    color: var(--white); font-size: 15px; font-weight: 800; text-transform: uppercase;
  }
  .services {
    position: absolute; left: 252px; top: 100px; width: 270px;
    list-style: none; color: var(--crimson);
    font-size: 13px; font-weight: 800; line-height: 1.3;
  }
  .services__item { display: flex; align-items: flex-start; gap: 5px; margin-bottom: 3.5px; }
  .services__tick { flex: 0 0 15px; width: 15px; height: 15px; margin-top: 1px; }
</style>
</head>
<body>

<section class="card card--front" aria-label="Business card front">
  <svg class="card__shapes" width="539" height="315" viewBox="0 0 539 315" aria-hidden="true">
    <polygon points="0,27 291,27 343,158 291,290 0,290" fill="var(--crimson)"/>
    <polygon points="299,27 317,27 369,158 317,290 299,290 351,158" fill="var(--maroon)"/>
  </svg>

  <div class="company">
    <div class="company__name">Mark Delaney Construction</div>
    <div class="company__trade">Concrete Contractor</div>
  </div>
  <div class="owner">Mark Delaney<span class="owner__role">Owner</span></div>

  <div class="contact-row" style="top:120px;height:26px;">
    <span class="contact-row__label">Business</span><span class="contact-row__value">334. 555. 0148</span>
  </div>
  <div class="contact-row" style="top:150px;height:26px;">
    <span class="contact-row__label">Mobile</span><span class="contact-row__value">334. 555. 0162</span>
  </div>
  <div class="contact-row" style="top:179px;height:26px;">
    <span class="contact-row__label">Home</span><span class="contact-row__value">334. 555. 0193</span>
  </div>
  <div class="contact-row" style="top:208px;height:29px;">
    <span class="contact-row__label">Address</span><span class="contact-row__value">218 West Millbrook Rd.<br>Oakridge, AL 36099</span>
  </div>
  <div class="contact-row" style="top:240px;height:27px;">
    <span class="contact-row__label">Email</span><span class="contact-row__value">mdconstruction1992@example.com</span>
  </div>

  <div class="brand">
    <div class="brand__mark"></div>
    <div class="brand__name">Mark Delaney Construction</div>
  </div>
  <div class="founder">
    <div class="founder__title">Founder</div>
    <div class="founder__name">Mark Delaney</div>
    <div class="founder__nick">“SLABMASTER”</div>
  </div>
</section>
<div class="side-label side-label--front">FRONT</div>

<section class="card card--back" aria-label="Business card back">
  <svg class="card__shapes" width="539" height="315" viewBox="0 0 539 315" aria-hidden="true">
    <rect x="0" y="0" width="29" height="315" fill="var(--maroon)"/>
    <polygon points="29,0 264,0 211,157 264,315 29,315" fill="var(--crimson)"/>
  </svg>

  <div class="specialty-heading">We Specializing In</div>

  <ul class="services">
    <li class="services__item">
      <svg class="services__tick" viewBox="0 0 16 16" aria-hidden="true"><path d="M12.5 4.5 A6 6 0 1 0 14 8" fill="none" stroke="var(--crimson)" stroke-width="1.4"/><path d="M4.5 7.5 L7.5 10.5 L15 2" fill="none" stroke="var(--crimson)" stroke-width="1.6"/></svg>
      <span>Metal building foundations</span>
    </li>
    <li class="services__item">
      <svg class="services__tick" viewBox="0 0 16 16" aria-hidden="true"><path d="M12.5 4.5 A6 6 0 1 0 14 8" fill="none" stroke="var(--crimson)" stroke-width="1.4"/><path d="M4.5 7.5 L7.5 10.5 L15 2" fill="none" stroke="var(--crimson)" stroke-width="1.6"/></svg>
      <span>Concrete foundations</span>
    </li>
    <li class="services__item">
      <svg class="services__tick" viewBox="0 0 16 16" aria-hidden="true"><path d="M12.5 4.5 A6 6 0 1 0 14 8" fill="none" stroke="var(--crimson)" stroke-width="1.4"/><path d="M4.5 7.5 L7.5 10.5 L15 2" fill="none" stroke="var(--crimson)" stroke-width="1.6"/></svg>
      <span>Driveways</span>
    </li>
    <li class="services__item">
      <svg class="services__tick" viewBox="0 0 16 16" aria-hidden="true"><path d="M12.5 4.5 A6 6 0 1 0 14 8" fill="none" stroke="var(--crimson)" stroke-width="1.4"/><path d="M4.5 7.5 L7.5 10.5 L15 2" fill="none" stroke="var(--crimson)" stroke-width="1.6"/></svg>
      <span>Storm rooms</span>
    </li>
    <li class="services__item">
      <svg class="services__tick" viewBox="0 0 16 16" aria-hidden="true"><path d="M12.5 4.5 A6 6 0 1 0 14 8" fill="none" stroke="var(--crimson)" stroke-width="1.4"/><path d="M4.5 7.5 L7.5 10.5 L15 2" fill="none" stroke="var(--crimson)" stroke-width="1.6"/></svg>
      <span>Additions and most other forms of concrete work.</span>
    </li>
  </ul>
</section>
<div class="side-label side-label--back">BACK</div>

</body>
</html>
```